Stationery Design for Tierhaven

We already have a logo a Logo for our outstanding veterinary hospital. Now we are looking for our future letterhead, business cards and envelopes. We would like to see a design using the color from our logo. Additional color should be limited to grey or a rusty brown. The font should be easy and clearly readable and must be easily available on all computers (to install it in our Management software). The finial design should communicate competence in veterinary medicine, and empathy.

To meet the European regulation (DIN5008) there are a couple mandatory legal informations one the letterhead. We also enclosed a template of exact measurement, which need to be respected according to DIN5008.

Mandatory legal information are (best placed in the footer):
"Tierhaven GmbH & Co KG, Ostrowgasse 417C, 1230 Wien,
Handelsgericht Wien, FN 924615k, GF: Dr. Lukas Brandl
ATU 3148926"
Additional informations needed:
"Tel: +43 1 5849163, Fax: +43 1 5849164, info@tierhaven-example.at, www. tierhaven-example.at"
bank account informations should be included as well. These are:
"Sparkasse Obergruntal, IBAN: AT 58 1111 2222 3333 4444, BIC: SPKTAT4K817"

The Logo should be in the upper right corner. Below that we need a space for informations regarding the responsible veterinarians. There will be 3-5 Names, each of it consisting of 2 lines (see example below). The Names should be highlighted (larger font) compared to the qualifications in the second line.
Tierärztliche Leitung:
Dr. Lukas Brandl
Diplomate ECVS

The contest was startet on the 2nd of may and the deadline was a day later? Why was that so fast? Did I do something wrong? BR

Target Market(s)

dog and cat owner in Austria as welle as referring veterinarians in Austria

Industry/Entity Type

Veterinary

Contact Information for Business Card

One side: Logo
other side:
Dr. Lukas Brandl
Diplomate ECVS
EBVS Specialist of Small Animal Surgery

Tierhaven GmbH&Co KG
Ostrowgasse 417C
1230 Wien

Tel: +43 1 6210000 DW 102
Fax: +43 1 6210000 DW 999
email: lukas.brandl@tierhaven-example.at

Font styles to use
Serif
Sans Serif

Requirements
Must have
• The logo should be given in the upper right. Most of the legal informations should be given in the footer. The upper left Area should be clear, since the recipient address will be placed there.
Colors should be limited to golden, blue and greyscale (two different gereysacales at most).

```html
<!DOCTYPE html>
<html lang="de">
<head>
<meta charset="utf-8">
<title>Tierhaven – Visitenkarte</title>
<link rel="stylesheet" href="https://fonts.googleapis.com/css2?family=Montserrat:wght@600;700&family=Open+Sans:wght@400;600&display=swap">
<style>
  :root{
    --navy:#1c2a5c;
    --gold:#e0a526;
    --paper:#ffffff;
    --ink:#1f2a44;
    --grey-bg:#d9dbde;
    --line:#2a3566;
  }
  *{box-sizing:border-box;margin:0;padding:0}
  html,body{width:1200px;height:960px;overflow:hidden}
  body{background:var(--grey-bg);font-family:"Open Sans",Arial,sans-serif;position:relative}
  .card{position:absolute;left:280px;width:640px;height:390px;box-shadow:0 6px 18px rgba(0,0,0,.18)}
  .card--front{top:40px;background:var(--navy)}
  .card--back{top:530px;background:var(--paper);color:var(--ink)}

  /* front */
  .front-brand{position:absolute;left:0;right:0;top:0;bottom:0;display:flex;align-items:center;justify-content:center;gap:26px}
  .brand-dot{width:140px;height:140px;border-radius:50%;border:6px solid var(--gold);background:var(--paper)}
  .brand-name{font-family:"Montserrat",Arial,sans-serif;font-weight:700;color:#fff;font-size:58px;line-height:1}
  .brand-tag{font-family:"Montserrat",Arial,sans-serif;font-weight:700;color:var(--gold);font-size:23px;margin-top:8px}

  /* back */
  .back-brand{position:absolute;right:44px;top:36px;display:flex;align-items:center;gap:12px}
  .back-brand .brand-dot{width:64px;height:64px;border-width:4px;background:var(--navy)}
  .back-brand .brand-name{color:var(--navy);font-size:28px}
  .back-brand .brand-tag{font-size:12px;margin-top:3px}
  .rule{position:absolute;height:1.5px;background:var(--line)}
  .rule--top{left:44px;right:44px;top:150px}
  .rule--short{left:44px;width:270px;top:262px}
  .person{position:absolute;left:44px;top:180px}
  .person-name{font-family:"Montserrat",Arial,sans-serif;font-weight:600;color:var(--navy);font-size:24px;line-height:1.1}
  .person-qual{font-size:13px;line-height:1.4;margin-top:4px}
  .address{position:absolute;right:44px;top:186px;text-align:right;font-size:15px;line-height:1.45}
  .contacts{position:absolute;left:44px;top:278px;list-style:none;font-size:15px;line-height:25px}
  .contacts li{display:flex;align-items:center;gap:10px}
  .contacts svg{width:14px;height:14px;fill:var(--navy);flex:none}
</style>
</head>
<body>
  <section class="card card--front">
    <div class="front-brand">
      <div class="brand-dot"></div>
      <div>
        <div class="brand-name">Tierhaven</div>
        <div class="brand-tag">Fachklinik für Kleintiere</div>
      </div>
    </div>
  </section>

  <section class="card card--back">
    <div class="back-brand">
      <div class="brand-dot"></div>
      <div>
        <div class="brand-name">Tierhaven</div>
        <div class="brand-tag">Fachklinik für Kleintiere</div>
      </div>
    </div>
    <div class="rule rule--top"></div>

    <div class="person">
      <div class="person-name">Dr. Lukas Brandl</div>
      <div class="person-qual">Diplomate ECVS<br>EBVS Specialist of Small Animal Surgery</div>
    </div>

    <address class="address" style="font-style:normal">
      Tierhaven GmbH&amp;Co KG<br>Ostrowgasse 417C<br>1230 Wien
    </address>

    <div class="rule rule--short"></div>

    <ul class="contacts">
      <li><svg viewBox="0 0 24 24"><path d="M6.6 10.8a15 15 0 0 0 6.6 6.6l2.2-2.2c.3-.3.7-.4 1-.2 1.1.4 2.3.6 3.6.6.6 0 1 .4 1 1V20c0 .6-.4 1-1 1C10.6 21 3 13.4 3 4c0-.6.4-1 1-1h3.5c.6 0 1 .4 1 1 0 1.3.2 2.5.6 3.6.1.3 0 .7-.2 1z"/></svg>+43 1 6210000 DW 102</li>
      <li><svg viewBox="0 0 24 24"><path d="M7 1h10a2 2 0 0 1 2 2v18a2 2 0 0 1-2 2H7a2 2 0 0 1-2-2V3a2 2 0 0 1 2-2zm0 3v14h10V4zm5 15.5a1 1 0 1 0 0 2 1 1 0 0 0 0-2z"/></svg>+43 1 6210000 DW 999</li>
      <li><svg viewBox="0 0 24 24"><path d="M2 5h20v14H2zm2 2v.5l8 5 8-5V7zm0 2.8V17h16V9.8l-8 5z"/></svg>lukas.brandl@tierhaven-example.at</li>
      <li><svg viewBox="0 0 24 24"><circle cx="12" cy="12" r="10"/></svg>www.tierhaven-example.at</li>
    </ul>
  </section>
</body>
</html>
```